Lanternwell Health - Professional Sales Presentation

Lanternwell Health needs to take it's professional sales presentation to the next level. The finished product must be engaging, elegant and trustworthy. In 20 slides or less, our value proposition needs to be crisply communicated. We will be using this presentation for Webinars and in print form, so this project requires a designer with deep powerpoint presentation experience. Both are very important ... 1) How the presentation is revealed live, and 2) How it appears in print form.

I've attached a draft presentation along with AI and JPG versions of our logo. Please visit LanternwellHealth.example for insight on our services. Be certain to watch the video on our home page to learn what we do ... you'll be inspired! The winning presentation will be presented in boardrooms at Summit 300 companies across America.

I'll interact frequently with those who take this project seriously and bring their very best work to the table ... you'll be working directly with Lanternwell's CEO.

You're invited to knock my socks off :)

Martin

Summit 300 Executives - the head of Benefits or Human Resources

Health Care

Sans Serif
Script

ec1f27

• Must be very professional, but creatively engaging, no more than 20 slides. Board rooms are inundated with BORING presentations ... that can't be this one. It needs to stand out, without going over the top.
• I need to be able to edit the text you'll find in my DRAFT presentation so please don't just create and use graphic files. Feel free to create cool graphic elements that are revealed at various points, but the next needs to be editable throughout.
• Can't be cheesy, cheap or gimmicky. Must be completely credible.

```html
<!DOCTYPE html>
<html lang="en">
<head>
<meta charset="utf-8">
<title>Lanternwell Health – Results</title>
<link rel="stylesheet" href="https://fonts.googleapis.com/css2?family=Open+Sans:wght@400;600;700&display=swap">
<style>
  :root {
    --brand-red: #ec1f27;
    --text-grey: #4d4d4d;
    --title-grey: #6d6d6d;
    --cube-blue: #5b9bd5;
    --cube-red: #ec1f27;
    --cube-yellow: #f0b429;
    --cube-green: #92d050;
    --bg-top: #ffffff;
    --bg-mid: #f1f1f1;
  }
  html, body { margin: 0; padding: 0; overflow: hidden; }
  body { width: 1200px; height: 899px; font-family: "Open Sans", Arial, sans-serif; }
  .slide {
    position: relative; width: 1200px; height: 899px; overflow: hidden;
    background: linear-gradient(to bottom, var(--bg-top) 0%, var(--bg-top) 30%, var(--bg-mid) 62%, var(--bg-top) 82%);
  }
  .slide-art { position: absolute; inset: 0; width: 1200px; height: 899px; }
  .page-number {
    position: absolute; left: 1160px; top: 8px; width: 30px; text-align: center;
    color: #fff; font-weight: 700; font-size: 19px;
  }
  .slide-title {
    position: absolute; left: 139px; top: 86px; margin: 0;
    font-weight: 400; font-size: 36px; color: var(--title-grey); letter-spacing: 0.2px;
  }
  .slide-title strong { color: var(--brand-red); font-weight: 700; }
  .callout {
    position: absolute; margin: 0; font-size: 15.3px; line-height: 22.3px; color: var(--text-grey);
  }
  .callout-01 { left: 723px; top: 250px; }
  .callout-04 { left: 58px; top: 320px; width: 300px; text-align: right; }
  .callout-03 { left: 35px; top: 451px; width: 200px; text-align: right; }
  .callout-02 { left: 891px; top: 443px; }
  .brand-name {
    position: absolute; left: 29px; top: 852px;
    font-size: 19px; font-weight: 600; color: var(--brand-red);
  }
  .footer-web {
    position: absolute; left: 0; width: 1206px; top: 845px; text-align: center;
    font-size: 13px; color: var(--brand-red);
  }
  .footer-copy {
    position: absolute; left: 0; width: 1206px; top: 864px; text-align: center;
    font-size: 9.5px; color: var(--text-grey);
  }
</style>
</head>
<body>
<main class="slide">
  <svg class="slide-art" viewBox="0 0 1021 765" aria-hidden="true">
    <defs>
      <linearGradient id="fade-blue" x1="0" y1="0" x2="0" y2="1">
        <stop offset="0" stop-color="#5b9bd5" stop-opacity="0.35"/><stop offset="1" stop-color="#5b9bd5" stop-opacity="0"/>
      </linearGradient>
      <linearGradient id="fade-red" x1="0" y1="0" x2="0" y2="1">
        <stop offset="0" stop-color="#ec1f27" stop-opacity="0.35"/><stop offset="1" stop-color="#ec1f27" stop-opacity="0"/>
      </linearGradient>
      <linearGradient id="fade-yellow" x1="0" y1="0" x2="0" y2="1">
        <stop offset="0" stop-color="#f0b429" stop-opacity="0.35"/><stop offset="1" stop-color="#f0b429" stop-opacity="0"/>
      </linearGradient>
      <linearGradient id="fade-green" x1="0" y1="0" x2="0" y2="1">
        <stop offset="0" stop-color="#92d050" stop-opacity="0.4"/><stop offset="1" stop-color="#92d050" stop-opacity="0"/>
      </linearGradient>
    </defs>

    <!-- page badge -->
    <circle cx="1005" cy="16" r="43" fill="var(--brand-red)"/>

    <!-- title marker -->
    <g fill="var(--brand-red)">
      <circle cx="57" cy="71" r="2.6"/>
      <circle cx="57" cy="79" r="2.6" opacity="0.85"/>
      <circle cx="57" cy="87" r="2.6" opacity="0.65"/>
      <circle cx="57" cy="95" r="2.6" opacity="0.45"/>
      <circle cx="57" cy="103" r="2.6" opacity="0.3"/>
    </g>

    <!-- reflections -->
    <polygon points="223,630 315,630 315,690 223,690" fill="url(#fade-blue)"/>
    <polygon points="315,630 345,601 345,660 315,690" fill="url(#fade-blue)" opacity="0.7"/>
    <polygon points="362,594 452,594 452,655 362,655" fill="url(#fade-red)"/>
    <polygon points="452,594 482,565 482,625 452,655" fill="url(#fade-red)" opacity="0.7"/>
    <polygon points="467,502 557,502 557,565 467,565" fill="url(#fade-yellow)"/>
    <polygon points="557,502 587,474 587,535 557,565" fill="url(#fade-yellow)" opacity="0.7"/>
    <polygon points="610,660 648,574 728,532 745,660" fill="url(#fade-green)"/>

    <!-- connector lines -->
    <g fill="none" stroke-width="1">
      <polyline points="525,388 525,240 607,240" stroke="var(--cube-yellow)"/>
      <polyline points="425,487 425,305 328,305" stroke="var(--cube-red)"/>
      <polyline points="284,520 284,455 215,455" stroke="var(--cube-blue)"/>
      <polyline points="662,443 662,356 835,356" stroke="#3fae3f"/>
    </g>

    <!-- cube 03 -->
    <polygon points="223,538 255,509 345,509 315,538" fill="#7fb2e2"/>
    <polygon points="315,538 345,509 345,600 315,628" fill="#4a80b5"/>
    <rect x="223" y="538" width="92" height="90" fill="var(--cube-blue)"/>
    <text x="266" y="590" text-anchor="middle" fill="#fff" font-family="Open Sans, Arial, sans-serif" font-weight="700" font-size="19">03</text>

    <!-- cube 04 -->
    <polygon points="362,502 392,473 482,473 452,502" fill="#f25158"/>
    <polygon points="452,502 482,473 482,563 452,592" fill="#bf1a21"/>
    <rect x="362" y="502" width="90" height="90" fill="var(--cube-red)"/>
    <text x="407" y="555" text-anchor="middle" fill="#fff" font-family="Open Sans, Arial, sans-serif" font-weight="700" font-size="19">04</text>

    <!-- cube 01 -->
    <polygon points="467,410 497,381 587,381 557,410" fill="#f3c55e"/>
    <polygon points="557,410 587,381 587,472 557,500" fill="#c9921c"/>
    <rect x="467" y="410" width="90" height="90" fill="var(--cube-yellow)"/>
    <text x="514" y="458" text-anchor="middle" fill="#fff" font-family="Open Sans, Arial, sans-serif" font-weight="700" font-size="19">01</text>

    <!-- cube 02 -->
    <polygon points="609,490 627,451 705,413 693,452" fill="#a9d97a" stroke="#6fb33a" stroke-width="0.8"/>
    <polygon points="693,452 705,413 743,492 728,531" fill="#6fad3e" stroke="#6fb33a" stroke-width="0.8"/>
    <polygon points="609,490 693,452 728,531 648,572" fill="var(--cube-green)" stroke="#6fb33a" stroke-width="0.8"/>
    <text x="676" y="521" text-anchor="middle" fill="#fff" font-family="Open Sans, Arial, sans-serif" font-weight="700" font-size="19">02</text>

    <!-- navigation -->
    <g fill="none" stroke="var(--brand-red)" stroke-width="1.4">
      <circle cx="947" cy="746" r="10.5"/>
      <polyline points="949,741 944,746 949,751"/>
      <circle cx="995" cy="746" r="10.5"/>
      <polyline points="993,741 998,746 993,751"/>
    </g>
  </svg>

  <div class="page-number">4</div>

  <h1 class="slide-title">… And The Results <strong>Speak</strong> For Themselves</h1>

  <p class="callout callout-01">More of your employees/spouses get their<br>Preventive Checkups!&nbsp; Realistic target of 80% is now<br>achievable as never before.</p>
  <p class="callout callout-04">Hypertensive &amp; pre-hypertensive<br>employees significantly improve their<br>numbers, too</p>
  <p class="callout callout-03">Diabetics and pre-<br>diabetics stay under<br>control over 3-4 years<br>much more so than<br>standard care (see<br>Lanternwell’s cohort study<br>trend line)</p>
  <p class="callout callout-02">100% of undiagnosed people get<br>diagnosed with diabetes,<br>hypertension, hyperlipidemia and<br>metabolic syndrome</p>

  <div class="brand-name">Lanternwell Health</div>
  <div class="footer-web">www.lanternwellhealth.example</div>
  <div class="footer-copy">©2015 Lanternwell Health • All Rights Reserved.</div>
</main>
</body>
</html>
```